Vantrell Law Letterhead

We need a new letterhead design for a Law Firm. The address for the law firm is 4817 Larkspur Boulevard, Suite 250, Houston, Texas 77342. Phone Number: 832-619-3057; Fax Number: 832-407-1694. The logo is uploaded to the project.

```html
<!DOCTYPE html>
<html lang="en">
<head>
<meta charset="utf-8">
<title>Vantrell Law Letterhead</title>
<link rel="stylesheet" href="https://fonts.googleapis.com/css2?family=Open+Sans:wght@400;600;700&display=swap">
<style>
  :root {
    --navy: #1b2f5c;
    --red: #d71f27;
    --grey-band: #dcdcdc;
    --backdrop: #e2e2e2;
    --paper: #ffffff;
    --ink: #3a3a3a;
    --rule: #dddddd;
    --sign-area: #eef0f4;
  }
  * { margin: 0; padding: 0; box-sizing: border-box; }
  html, body { width: 1200px; height: 1200px; overflow: hidden; }
  body {
    background: var(--backdrop);
    font-family: "Open Sans", Arial, sans-serif;
    color: var(--ink);
    position: relative;
  }
  .sheet {
    position: absolute;
    left: 228px; top: 74px;
    width: 744px; height: 1052px;
    background: var(--paper);
    overflow: hidden;
  }
  .band { position: absolute; left: 0; width: 744px; }
  .band-top { top: 0; height: 49px; }
  .band-bottom { top: 1002px; height: 50px; }
  .recipient { position: absolute; left: 74px; top: 101px; }
  .recipient .label { font-size: 14.5px; font-weight: 700; color: #222; line-height: 22px; }
  .recipient .name { font-size: 15.5px; font-weight: 700; color: var(--red); line-height: 26px; }
  .recipient .role { font-size: 12px; line-height: 22px; }
  .contact { position: absolute; left: 74px; top: 188px; font-size: 12px; line-height: 30px; }
  .brand {
    position: absolute; left: 494px; top: 116px;
    display: flex; align-items: center; gap: 10px;
  }
  .brand .mark { width: 34px; height: 34px; background: var(--navy); }
  .brand .name { font-size: 25px; font-weight: 600; color: var(--navy); letter-spacing: 0.3px; }
  .letter-body {
    position: absolute; left: 74px; top: 301px; width: 596px;
    font-size: 15px; line-height: 33px; text-align: justify;
  }
  .letter-body p + p { margin-top: 33px; }
  .office {
    position: absolute; left: 74px; top: 837px; width: 229px;
    border-top: 1px solid var(--rule); border-bottom: 1px solid var(--rule);
    padding: 10px 0 12px; font-size: 12px; line-height: 24px;
  }
  .office strong { font-weight: 700; }
  .signatory { position: absolute; left: 428px; top: 843px; }
  .signatory .signature { width: 100px; height: 38px; background: var(--sign-area); border-radius: 3px; }
  .signatory .name { font-size: 15px; font-weight: 700; margin-top: 4px; line-height: 22px; }
  .signatory .title { font-size: 12px; line-height: 24px; }
</style>
</head>
<body>
  <div class="sheet">
    <svg class="band band-top" viewBox="0 0 744 49" aria-hidden="true">
      <polygon points="0,0 348,0 367,49 0,49" fill="var(--navy)"/>
      <polygon points="355,16 558,16 589,49 370,49" fill="var(--red)"/>
      <polygon points="580,16 744,16 744,49 611,49" fill="var(--grey-band)"/>
    </svg>

    <div class="recipient">
      <div class="label">To</div>
      <div class="name">Marlon Pettigrew</div>
      <div class="role">Trainer &amp; Manager, Company Name</div>
    </div>
    <div class="contact">
      <div>P: 832-619-3057</div>
      <div>E: office@vantrelllaw.com</div>
      <div>W: vantrelllaw.com</div>
    </div>

    <div class="brand">
      <span class="mark"></span>
      <span class="name">Vantrell Law</span>
    </div>

    <div class="letter-body">
      <p>A letterhead is the heading at the top of a sheet of letter paper (stationery). That heading usually consists of a name and an address, and a logo or corporate design, and sometimes a background pattern.</p>
      <p>The term "letterhead" is often used to refer to the whole sheet imprinted with such a heading. Many companies and individuals prefer to create a letterhead template in a word processor or other software application. This generally includes the same information as pre-printed stationery but without the additional costs involved. Letterhead can then be printed on stationery (or plain paper) as needed on a local output device or sent electronically.</p>
      <p>That heading usually consists of a name and an address, and a logo or corporate design, and sometimes a background pattern. The term "letterhead" is often used to refer to the whole sheet imprinted with such a heading.</p>
    </div>

    <div class="office">
      <div>4817 Larkspur Boulevard, Suite 250</div>
      <div>Houston, Texas 77342</div>
      <div>Ph. <strong>832-619-3057</strong></div>
      <div>Fax. <strong>832-407-1694</strong></div>
    </div>

    <div class="signatory">
      <div class="signature" role="img" aria-label="Handwritten signature of Elena Marquette"></div>
      <div class="name">Elena Marquette</div>
      <div class="title">Director</div>
    </div>

    <svg class="band band-bottom" viewBox="0 0 744 50" aria-hidden="true">
      <polygon points="0,0 138,0 187,50 0,50" fill="var(--navy)"/>
      <polygon points="161,0 744,0 744,32 192,32" fill="var(--red)"/>
    </svg>
  </div>
</body>
</html>
```